New Business Card Design Project

We require a business card design for Pharvelix, a newly established Indian company.
Our focus is on the development, manufacturing, and export of a diverse array of pharmaceutical products on a global scale. The card should convey a professional appearance, as our primary markets are in Africa, China, and Southeast Asian nations.
We envision a two-sided business card, with the reverse side dedicated to a logo set against a solid color or an elegantly designed pattern. The corners should be rounded. We would appreciate seeing both horizontal and vertical design options. We trust the designer to utilize their expertise in creating this design.

The content for the business card is included in the attached Word file.

Target Market(s)

Our primary markets are in Africa, China, and Southeast Asian, Latin America, Maldives, Sri Lanka

Industry/Entity Type

Pharmaceutical Manufacturing and Export

Contact Information for Business Card

Colors

Designer to choose colors to be used in the design.

Requirements
Must have
• The reverse side of the business card features solely the logo along with the tagline, "Care Beyond Borders."
Should not have
• The logo should not exceed two instances, encompassing both the front and back sides of the card.

```html
<!DOCTYPE html>
<html lang="en">
<head>
<meta charset="UTF-8">
<title>Pharvelix Business Card</title>
<link href="https://fonts.googleapis.com/css2?family=Montserrat:wght@400;500;700;800&display=swap" rel="stylesheet">
<style>
  :root {
    --page-bg: #e9e6e1;
    --brand-blue: #239fd6;
    --brand-blue-deep: #0f5573;
    --brand-blue-mid: #1b86b6;
    --accent-red: #e85c4a;
    --ink: #3a3a3a;
    --card-white: #ffffff;
    --card-grey: #ececec;
  }
  * { margin: 0; padding: 0; box-sizing: border-box; }
  html, body {
    width: 1200px; height: 900px; overflow: hidden;
    background: var(--page-bg);
    font-family: "Montserrat", sans-serif;
  }
  .canvas { position: relative; width: 1200px; height: 900px; }
  .card {
    position: absolute; left: 260px; width: 680px; height: 388px;
    border-radius: 34px; overflow: hidden;
    box-shadow: 0 14px 30px rgba(0,0,0,0.22);
  }
  /* Reverse side */
  .card--back {
    top: 40px;
    background: radial-gradient(ellipse at 40% 70%, var(--brand-blue) 0%, var(--brand-blue-mid) 40%, var(--brand-blue-deep) 100%);
  }
  .tagline {
    position: absolute; top: 34px; right: 52px;
    color: var(--card-white); font-weight: 700; font-size: 17px;
    letter-spacing: 5px; white-space: nowrap;
  }
  .tagline-marker {
    position: absolute; top: 36px; right: 0;
    width: 0; height: 0;
    border-top: 11px solid transparent; border-bottom: 11px solid transparent;
    border-right: 20px solid var(--card-white);
  }
  .back-brand {
    position: absolute; left: 170px; top: 200px;
    display: flex; align-items: center; gap: 18px;
  }
  .brand-dot {
    width: 34px; height: 34px; border-radius: 50%;
    background: var(--card-white);
  }
  .brand-name {
    font-weight: 800; font-size: 64px; color: var(--card-white);
    letter-spacing: 1px; white-space: nowrap;
  }
  /* Front side */
  .card--front {
    top: 472px;
    background: linear-gradient(135deg, var(--card-white) 0%, var(--card-grey) 55%, var(--card-white) 100%);
  }
  .name-marker {
    position: absolute; left: 0; top: 46px;
    border-top: 11px solid transparent; border-bottom: 11px solid transparent;
    border-left: 18px solid var(--brand-blue);
  }
  .contact { position: absolute; left: 44px; top: 38px; color: var(--ink); }
  .contact-name {
    color: var(--brand-blue); font-weight: 800; font-size: 22px; letter-spacing: 0.5px;
  }
  .contact-role { font-size: 17px; margin-top: 2px; }
  .contact-address { font-size: 17px; line-height: 1.3; margin-top: 30px; }
  .contact-lines { list-style: none; margin-top: 26px; font-size: 17px; }
  .contact-lines li { display: flex; align-items: center; gap: 12px; margin-bottom: 8px; white-space: nowrap; }
  .contact-lines svg { width: 18px; height: 18px; flex: none; }
  .front-brand {
    position: absolute; right: 52px; top: 286px;
    display: flex; align-items: center; gap: 14px;
  }
  .front-brand .brand-dot { background: var(--accent-red); width: 28px; height: 28px; }
  .front-brand .brand-name { color: var(--brand-blue); font-size: 54px; }
</style>
</head>
<body>
<main class="canvas">
  <section class="card card--back" aria-label="Card reverse side">
    <p class="tagline">Care Beyond Borders</p>
    <span class="tagline-marker"></span>
    <div class="back-brand">
      <span class="brand-dot"></span>
      <span class="brand-name">Pharvelix</span>
    </div>
  </section>

  <section class="card card--front" aria-label="Card front side">
    <span class="name-marker"></span>
    <div class="contact">
      <h1 class="contact-name">ROHAN K. DESAI</h1>
      <p class="contact-role">CEO Of Pharvelix</p>
      <p class="contact-address">12, Lotus Park<br>Nashik, 422001, India</p>
      <ul class="contact-lines">
        <li>
          <svg viewBox="0 0 18 18"><rect x="4" y="1" width="10" height="16" rx="2" fill="none" stroke="var(--accent-red)" stroke-width="1.6"/><line x1="8" y1="14" x2="10" y2="14" stroke="var(--accent-red)" stroke-width="1.6"/></svg>
          +919812345670
        </li>
        <li>
          <svg viewBox="0 0 18 18"><rect x="1" y="4" width="16" height="11" fill="var(--accent-red)"/><polyline points="1,4 9,10 17,4" fill="none" stroke="#fff" stroke-width="1.4"/></svg>
          rdesai@pharvelix.com
        </li>
        <li>
          <svg viewBox="0 0 18 18"><circle cx="9" cy="9" r="7.5" fill="none" stroke="var(--accent-red)" stroke-width="1.4"/><ellipse cx="9" cy="9" rx="3.2" ry="7.5" fill="none" stroke="var(--accent-red)" stroke-width="1.2"/><line x1="1.5" y1="9" x2="16.5" y2="9" stroke="var(--accent-red)" stroke-width="1.2"/></svg>
          www.pharvelix.com
        </li>
      </ul>
    </div>
    <div class="front-brand">
      <span class="brand-dot"></span>
      <span class="brand-name">Pharvelix</span>
    </div>
  </section>
</main>
</body>
</html>
```